Medicinal Cannabis Patient Monitoring App

We have a BASIC design for our app for monitoring patients who received Medicinal Cannabis.
The patient would rate how they're feeling after each dose.

The general flow once user is logged in and set up in the system is:

- User should be able to enter the dosing information for the current day
* Consumption Details:
> Enter Time
> Enter Dosage Taken (Added during onboarding)
> Method take to consume the drug
* Score Details:
> Pain Score (On the scale of 1-10)
> Nausea Score (On the scale of 1-10)
> Sedation Score (On the scale of 1-10)
> Wellbeing Score (On the scale of 1-10)
* Blood Pressure Details:
> Pulse
> Blood Pressure Readings
- User should be able to view the instructions
- User should be able to submit the entered details in the platform

We're looking for a clean, medical and SIMPLE design.

OUR USERS are often ELDERLY, Children and disabled individuals. You must consider this in the design.
So, for example, when designing sliders you should consider a creative way to explain the meaning of the slider if the person cant read the word description.

Designs look the same

```html
<!DOCTYPE html>
<html lang="en">
<head>
<meta charset="utf-8">
<title>How are you feeling?</title>
<link href="https://fonts.googleapis.com/css2?family=Open+Sans:wght@400;600;700;800&display=swap" rel="stylesheet">
<style>
:root{
  --green:#33c97a;
  --green-soft:#8fdcb2;
  --ink:#3b3f44;
  --muted:#b3b7bb;
  --track:#ededed;
  --rule:#e4e4e4;
  --chip:#ececec;
  --bg:#ffffff;
}
*{box-sizing:border-box;margin:0;padding:0}
html,body{width:1200px;height:2368px;overflow:hidden;background:var(--bg)}
body{font-family:"Open Sans",Arial,sans-serif;color:var(--ink)}
.screen{position:absolute;left:0;top:0;width:375px;height:740px;transform:scale(3.2);transform-origin:0 0;background:var(--bg)}
.status-bar{position:absolute;left:0;top:0;width:375px;height:20px;font-size:12px;font-weight:600;color:#111}
.status-bar .carrier{position:absolute;left:5px;top:3px;display:flex;align-items:center;gap:4px}
.status-bar .time{position:absolute;left:0;right:0;top:3px;text-align:center}
.status-bar .power{position:absolute;right:5px;top:3px;display:flex;align-items:center;gap:4px}
.nav{position:absolute;left:0;top:20px;width:375px;height:50px}
.nav .back{position:absolute;left:7px;top:14px;font-size:15px;font-weight:600;color:var(--green);display:flex;align-items:center;gap:3px}
.nav .step{position:absolute;left:0;right:0;top:7px;text-align:center;font-size:9.5px;letter-spacing:2px;color:#555}
.nav .title{position:absolute;left:0;right:0;top:19px;text-align:center;font-size:16px;font-weight:700;color:#333}
.nav .help{position:absolute;left:335px;top:11px}
.progress{position:absolute;left:0;top:70px;width:375px;height:4px;background:var(--track)}
.progress .done{width:193px;height:100%;background:var(--green)}
.rating{position:absolute;left:0;width:375px;border-bottom:1px solid var(--rule)}
.rating .label{position:absolute;left:0;right:0;display:flex;justify-content:center;align-items:center;gap:8px;font-size:16px;font-weight:700;color:#444}
.rating .slider{position:absolute;left:13px;width:350px;height:4px;border-radius:2px;background:var(--track)}
.rating .fill{position:absolute;left:0;top:0;height:4px;border-radius:2px;background:var(--green-soft);width:calc(var(--thumb) - 13px)}
.rating .thumb{position:absolute;top:-12px;left:calc(var(--thumb) - 13px - 14px);width:28px;height:28px;border-radius:50%;background:var(--green)}
.rating .scale{position:absolute;left:5px;width:362px;display:flex;justify-content:space-between}
.rating .scale span{width:22px;height:22px;line-height:22px;text-align:center;font-size:12.5px;color:var(--muted)}
.rating .scale span.picked{background:var(--chip);border-radius:50%;color:#333;font-weight:700;font-size:14px}
.pain{top:74px;height:155px}
.nausea{top:229px;height:146px}
.sedation{top:375px;height:144px}
.wellbeing{top:519px;height:142px}
.pain .label{top:32px}.pain .slider{top:85px}.pain .scale{top:103px}
.nausea .label{top:26px}.nausea .slider{top:79px}.nausea .scale{top:98px}
.sedation .label{top:25px}.sedation .slider{top:78px}.sedation .scale{top:97px}
.wellbeing .label{top:23px}.wellbeing .slider{top:76px}.wellbeing .scale{top:95px}
.next{position:absolute;left:10px;top:672px;width:355px;height:58px;border-radius:29px;background:var(--green);color:#fff;font-size:16px;font-weight:700;display:flex;align-items:center;justify-content:center;gap:8px}
</style>
</head>
<body>
<div class="screen">
  <div class="status-bar">
    <div class="carrier">
      <svg width="18" height="10" viewBox="0 0 18 10"><rect x="0" y="7" width="3" height="3" fill="#111"/><rect x="4" y="5" width="3" height="5" fill="#111"/><rect x="8" y="3" width="3" height="7" fill="#111"/><rect x="12" y="0" width="3" height="10" fill="#111"/></svg>
      <span>Linko</span>
      <svg width="14" height="10" viewBox="0 0 14 10"><path d="M1 3.5a8.5 8.5 0 0 1 12 0M3 5.6a5.5 5.5 0 0 1 8 0M5 7.7a2.5 2.5 0 0 1 4 0" fill="none" stroke="#111" stroke-width="1.5"/></svg>
    </div>
    <div class="time">9:41 AM</div>
    <div class="power">
      <svg width="7" height="12" viewBox="0 0 7 12"><path d="M1 3l5 5-2.5 2.5V1.5L6 4 1 9" fill="none" stroke="#111" stroke-width="1.2"/></svg>
      <span>100%</span>
      <svg width="25" height="11" viewBox="0 0 25 11"><rect x="0.5" y="0.5" width="21" height="10" rx="2.5" fill="none" stroke="#111"/><rect x="2" y="2" width="18" height="7" rx="1.5" fill="#111"/><rect x="22.5" y="3.5" width="2" height="4" rx="1" fill="#111"/></svg>
    </div>
  </div>

  <header class="nav">
    <div class="back">
      <svg width="10" height="14" viewBox="0 0 10 14"><path d="M8 1.5 2.5 7 8 12.5" fill="none" stroke="#33c97a" stroke-width="2"/></svg>
      <span>Back</span>
    </div>
    <div class="step">STEP TWO</div>
    <h1 class="title">How are you feeling?</h1>
    <svg class="help" width="26" height="26" viewBox="0 0 26 26"><circle cx="13" cy="13" r="11.5" fill="none" stroke="#33c97a" stroke-width="2"/><text x="13" y="18" text-anchor="middle" font-family="Open Sans, sans-serif" font-weight="800" font-size="14" fill="#33c97a">?</text></svg>
  </header>

  <div class="progress"><div class="done"></div></div>

  <section class="rating pain" style="--thumb:129px">
    <div class="label"><svg width="28" height="28" viewBox="0 0 28 28"><circle cx="14" cy="14" r="11" fill="none" stroke="#33c97a" stroke-width="2"/></svg><span>Pain</span></div>
    <div class="slider"><div class="fill"></div><div class="thumb"></div></div>
    <div class="scale"><span>1</span><span>2</span><span>3</span><span class="picked">4</span><span>5</span><span>6</span><span>7</span><span>8</span><span>9</span><span>10</span></div>
  </section>

  <section class="rating nausea" style="--thumb:91px">
    <div class="label"><svg width="28" height="28" viewBox="0 0 28 28"><circle cx="14" cy="14" r="11" fill="none" stroke="#33c97a" stroke-width="2"/></svg><span>Nausea</span></div>
    <div class="slider"><div class="fill"></div><div class="thumb"></div></div>
    <div class="scale"><span>1</span><span>2</span><span class="picked">3</span><span>4</span><span>5</span><span>6</span><span>7</span><span>8</span><span>9</span><span>10</span></div>
  </section>

  <section class="rating sedation" style="--thumb:278px">
    <div class="label"><svg width="28" height="28" viewBox="0 0 28 28"><circle cx="14" cy="14" r="11" fill="none" stroke="#33c97a" stroke-width="2"/></svg><span>Sedation</span></div>
    <div class="slider"><div class="fill"></div><div class="thumb"></div></div>
    <div class="scale"><span>1</span><span>2</span><span>3</span><span>4</span><span>5</span><span>6</span><span>7</span><span class="picked">8</span><span>9</span><span>10</span></div>
  </section>

  <section class="rating wellbeing" style="--thumb:91px">
    <div class="label"><svg width="28" height="28" viewBox="0 0 28 28"><circle cx="14" cy="14" r="11" fill="none" stroke="#33c97a" stroke-width="2"/></svg><span>Wellbeing</span></div>
    <div class="slider"><div class="fill"></div><div class="thumb"></div></div>
    <div class="scale"><span>1</span><span>2</span><span>3</span><span>4</span><span>5</span><span class="picked">6</span><span>7</span><span>8</span><span>9</span><span>10</span></div>
  </section>

  <div class="next">
    <span>Next</span>
    <svg width="18" height="14" viewBox="0 0 18 14"><path d="M1 7h15M10 1.5 16 7l-6 5.5" fill="none" stroke="#fff" stroke-width="2"/></svg>
  </div>
</div>
</body>
</html>
```